Landscape Company in need of logo and business card update. Current logo file is attached.

I need a business card design for a Woman Owned Landscape business in Kansas City. I do Native plant installation and maintenance as well as mowing, chemical applications and residential and commercial landscaping.
My colors are navy, green and white.
I currently have a logo that can be used or you can redesign it.

Target Market(s)

Residential and commercial

Industry/Entity Type

Landscape

Contact Information for Business Card

On back of current card it lists what I do and website:
BMP/Raingarden Maintenance and Installation, Certified Chemical Applicator for Trees, shrubs, and turf; Landscape Design and Installation for residential and commercial.

Logo Text

Copperleaf Landscape Services, LLC

Font styles to use
Other font styles liked:
• See current font on logo examples

Requirements
Must have
• Phone number: 816-402-7719
• Website: www.copperleaflandscape-example.com
• Colors: Navy, Green, white
• Email: copperleaflandscape@mailbox-example.com
• Address: PO BOX 471208 Shawnee, KS 66219
• Name of Person: Marcy Dulwick, owner

```html
<!DOCTYPE html>
<html lang="en">
<head>
<meta charset="utf-8">
<title>Copperleaf Landscape – Identity and Business Card</title>
<link rel="stylesheet" href="https://fonts.googleapis.com/css2?family=Arimo:wght@400;700&display=swap">
<style>
  :root {
    --green: #6ab344;
    --green-light: #8cc665;
    --grey: #a9a9a9;
    --grey-text: #9a9a9a;
    --charcoal: #3a3a3c;
    --white: #ffffff;
    --stage: #ebe8e4;
  }
  * { box-sizing: border-box; margin: 0; padding: 0; }
  html, body { width: 1098px; height: 1200px; overflow: hidden; }
  body {
    position: relative;
    background: var(--stage);
    font-family: "Arimo", Arial, sans-serif;
  }
  .brand-panel {
    position: absolute; top: 0; height: 283px; width: 549px;
    display: flex; align-items: center; justify-content: center;
  }
  .brand-panel--dark { left: 0; background: var(--charcoal); }
  .brand-panel--light { left: 549px; background: var(--white); }
  .wordmark {
    font-weight: 700; color: var(--green);
    white-space: nowrap; letter-spacing: 0.5px;
  }
  .brand-panel .wordmark { font-size: 40px; }

  .card {
    position: absolute; left: 242px; width: 609px; height: 361px;
    background: var(--white); border-radius: 24px; overflow: hidden;
    box-shadow: 0 4px 12px rgba(0,0,0,0.18);
  }
  .card--front { top: 355px; }
  .card--back { top: 775px; }

  .owner-name {
    position: absolute; left: 30px; top: 78px;
    font-size: 22px; font-weight: 700; color: var(--green);
  }
  .owner-title {
    position: absolute; left: 30px; top: 106px;
    font-size: 15px; font-weight: 700; color: var(--grey-text);
  }
  .card--front .wordmark {
    position: absolute; right: 32px; top: 140px;
    text-align: right; font-size: 22px;
  }
  .contact-list { position: absolute; left: 30px; top: 188px; list-style: none; }
  .contact-item {
    display: flex; align-items: flex-start; gap: 6px;
    font-size: 15px; line-height: 20px; color: var(--grey-text);
    margin-bottom: 5px;
  }
  .contact-item--address { margin-bottom: 19px; }
  .contact-item svg { flex: none; margin-top: 3px; }
  .front-wave { position: absolute; left: 0; bottom: 0; }
  .front-url {
    position: absolute; right: 30px; bottom: 26px;
    font-size: 15px; color: var(--white);
  }

  .card--back .wordmark {
    position: absolute; left: 0; right: 0; top: 104px;
    text-align: center; font-size: 34px;
  }
  .services {
    position: absolute; left: 40px; right: 40px; top: 228px;
    text-align: center; font-size: 16px; line-height: 23px; color: var(--green);
  }
  .back-url {
    position: absolute; left: 0; right: 0; top: 320px;
    text-align: center; font-size: 15px; letter-spacing: 1.3px; color: var(--grey-text);
  }
  .back-url .domain { color: var(--green); }
</style>
</head>
<body>
  <section class="brand-panel brand-panel--dark">
    <span class="wordmark">Copperleaf Landscape</span>
  </section>
  <section class="brand-panel brand-panel--light">
    <span class="wordmark">Copperleaf Landscape</span>
  </section>

  <article class="card card--front">
    <h1 class="owner-name">Marcy Dulwick</h1>
    <p class="owner-title">Owner</p>
    <span class="wordmark">Copperleaf Landscape</span>
    <ul class="contact-list">
      <li class="contact-item contact-item--address">
        <svg width="12" height="16" viewBox="0 0 12 16"><path d="M6 1a5 5 0 0 1 5 5c0 3.5-5 9-5 9S1 9.5 1 6a5 5 0 0 1 5-5z" fill="none" stroke="var(--green)" stroke-width="1.6"/><circle cx="6" cy="6" r="1.8" fill="var(--green)"/></svg>
        <span>PO BOX 471208 Shawnee,<br>KS 66219</span>
      </li>
      <li class="contact-item">
        <svg width="14" height="14" viewBox="0 0 14 14"><path d="M1 5c0-2 2-3 6-3s6 1 6 3v1h-3V5H4v1H1z" fill="var(--green)"/><rect x="2.5" y="6.5" width="9" height="6" rx="1.5" fill="var(--green)"/><circle cx="7" cy="9.5" r="1.6" fill="var(--white)"/></svg>
        <span>816-402-7719</span>
      </li>
      <li class="contact-item">
        <svg width="14" height="14" viewBox="0 0 14 14"><rect x="1" y="3" width="12" height="8" fill="var(--green)"/><path d="M1 3l6 4.5L13 3" fill="none" stroke="var(--white)" stroke-width="1.2"/></svg>
        <span>copperleaflandscape@mailbox-example.com</span>
      </li>
    </ul>
    <svg class="front-wave" width="609" height="80" viewBox="0 0 609 80">
      <path d="M0 8 C150 30 300 36 420 22 C500 12 560 4 609 6 L609 80 L0 80 Z" fill="var(--green-light)"/>
      <path d="M0 18 C160 36 310 40 430 28 C510 20 565 14 609 16 L609 80 L0 80 Z" fill="var(--green)"/>
      <path d="M0 10 C120 30 250 40 360 36 C250 46 120 40 0 22 Z" fill="#c8c8c8"/>
    </svg>
    <span class="front-url">www.copperleaflandscape-example.com</span>
  </article>

  <article class="card card--back">
    <span class="wordmark">Copperleaf Landscape</span>
    <p class="services">BMP/Raingarden Maintenance and Installation, Certified Chemical Applicator for Trees, shrubs, and turf; Landscape Design and Installation for residential and commercial.</p>
    <p class="back-url">www.<span class="domain">copperleaflandscape-example</span>.com</p>
  </article>
</body>
</html>
```